Feng shui business card for immigration law firm

Immigration law firm would like to create the business card based and look like the Green Card (lawful permanent resident card of USA). Attached please see the sample of American Green Card. The whole business card should be performed based on the FENG SHUI style: no sharp angles. Please delete all letters and fingerprint on the sample green card and put info the following order.

Target Market(s)

Immigration clients in USA

Industry/Entity Type

Business

Contact Information for Business Card

Immigration law firm would like to create the business card based and look like the Green Card (lawful permanent resident card of USA). Attached please see the sample of American Green Card. The whole business card should be performed based on the FENG SHUI style: no sharp angles. Please delete all letters on sample green card and put info the following order:

TOLAN BERIKSOVA, ESQ.
BERIKSOVA LAW GROUP, P.A.
PRACTICE LIMITED TO IMMIGRATION LAW

4370 WEST CORVINDALE PARK BOULVERD
SUITE #218
CORVINDALE PARK, FLORIDA 33174

PHONE: 754-555-0162
EMAIL: TBERIKSOVA@QUELMAIL.EXAMPLE
WEBSITE: WWW.ZORVEL-VISAHELP.EXAMPLE

The tips for the best business card
1. It is recommended to avoid using sharp points in the logo because such logos generate negative energy. Never use sharp and pointed element like spears, knives or swords in your logo.
2. One of the most essential elements in Feng Shui good flow and space which means that there should not be any obstruction, for example, there should not be any border around the card as it stop the energy flow.
3. Keep clear of clutter – Just like applying this feng shui concept to home and office, it should also be applied to designing your name card. Always keep your card as clean and concise as possible by removing all redundant information and put only relevant ones.
4. Name should not be placed in the center of the card because it cause stress and pressure to the owner.

Font styles to use
Other font styles liked:
• Garamond or Times New Roman

Requirements
Must have
• Feng shui business card

```html
<!DOCTYPE html>
<html lang="en">
<head>
<meta charset="utf-8">
<title>Beriksova Law Group – Business Card</title>
<link rel="stylesheet" href="https://fonts.googleapis.com/css2?family=Barlow:wght@400;500&display=swap">
<style>
  :root {
    --stage: #24272c;
    --card-green: #3d7558;
    --card-green-light: #9ec9b4;
    --paper: #f6f4ea;
    --pale-teal: #cfe6e2;
    --deep-teal: #4fb6bd;
    --ink: #111111;
    --white: #ffffff;
    --sky-deep: #1d4aa3;
    --sky-light: #2e62c0;
  }
  * { margin: 0; padding: 0; box-sizing: border-box; }
  html, body { width: 1200px; height: 1000px; overflow: hidden; }
  body {
    background: var(--stage);
    font-family: "Barlow", Arial, sans-serif;
    color: var(--ink);
    position: relative;
  }
  .card {
    position: absolute;
    left: 245px;
    width: 712px;
    border-radius: 22px;
    overflow: hidden;
  }
  .card-front { top: 118px; height: 395px; background: var(--paper); }
  .card-back  { top: 530px; height: 393px; }

  .front-artwork {
    position: absolute; inset: 0;
    background:
      radial-gradient(ellipse 240px 220px at 600px 290px, var(--deep-teal) 0%, rgba(79,182,189,0.45) 45%, rgba(79,182,189,0) 100%),
      linear-gradient(100deg, #eef3ea 0%, var(--pale-teal) 35%, #e8f0ea 60%, #f3f1e4 100%);
  }
  .name-band {
    position: absolute; left: 0; top: 0;
    width: 347px; height: 80px;
    background: var(--card-green);
  }
  .firm-band {
    position: absolute; left: 347px; top: 0;
    width: 365px; height: 98px;
    background: var(--card-green);
  }
  .firm-band-strip {
    position: absolute; left: 13px; top: 0; right: 0; height: 17px;
    background: linear-gradient(90deg, var(--card-green-light), #c9e0d4);
  }
  .holder-name {
    position: absolute; left: 27px; top: 30px;
    color: var(--white); font-size: 22px; font-weight: 500; letter-spacing: 0.5px;
  }
  .firm-name {
    position: absolute; left: 33px; top: 35px;
    color: var(--white); font-size: 17px; font-weight: 500; letter-spacing: 0.3px;
  }
  .firm-practice {
    position: absolute; left: 33px; top: 58px;
    color: var(--white); font-size: 13.5px;
  }
  .address {
    position: absolute; left: 55px; top: 130px;
    font-size: 16px; line-height: 24px; letter-spacing: 0.4px;
  }
  .contact { position: absolute; left: 103px; }
  .contact-label { font-size: 18px; line-height: 20px; }
  .contact-value { font-size: 23px; line-height: 26px; font-weight: 500; }
  .contact-phone   { top: 201px; }
  .contact-email   { top: 266px; }
  .contact-website { top: 326px; }

  .back-photo {
    position: absolute; inset: 0;
    background:
      radial-gradient(ellipse 80px 90px at 40px 340px, rgba(255,255,255,0.85), rgba(255,255,255,0) 100%),
      linear-gradient(160deg, var(--sky-light), var(--sky-deep));
  }
</style>
</head>
<body>
  <section class="card card-front">
    <div class="front-artwork" role="img" aria-label="Pale security-print background with a faint teal statue motif"></div>
    <div class="name-band">
      <div class="holder-name">TOLAN BERIKSOVA, ESQ.</div>
    </div>
    <div class="firm-band">
      <div class="firm-band-strip"></div>
      <div class="firm-name">BERIKSOVA LAW GROUP, P.A.</div>
      <div class="firm-practice">Practice Limited To Immigration Law</div>
    </div>
    <div class="address">
      4370 WEST CORVINDALE PARK BOULVERD<br>
      SUITE #218 CORVINDALE PARK, FLORIDA 33174
    </div>
    <div class="contact contact-phone">
      <div class="contact-label">Phone</div>
      <div class="contact-value">754-555-0162</div>
    </div>
    <div class="contact contact-email">
      <div class="contact-label">Email</div>
      <div class="contact-value">tberiksova@quelmail.example</div>
    </div>
    <div class="contact contact-website">
      <div class="contact-label">Website</div>
      <div class="contact-value">www.zorvel-visahelp.example</div>
    </div>
  </section>

  <section class="card card-back">
    <div class="back-photo" role="img" aria-label="Photograph of the United States flag waving on a flagpole against a deep blue sky"></div>
  </section>
</body>
</html>
```